Democracy in crisis book

This book tries to sound the ALARM that we will lose our democracy unless we force Unionists to adopt the plan inside this book. I designed a mock cover (attached) but I am concerned it would not look good in the Thumbnail view that most people would see it as they're scrolling down Shopvale or Pagenook. The final title for the book is: Final Hour to Rescue the Free Republic. The current subtitle is: The Single Path to Halt the 2022 Partisan Takeover & Renew Our Homeland -- but it’s a work in progress.The subtitle is still working progress but it's really not that important and can be small.
STYLE CONSIDERATIONS:
(1) The title should be on 5 separate lines: Final; Hour; To Rescue; Free; Republic
(2) The title could be in white fat letters except for maybe one line that says “To Rescue” which could be in the blue color of the Civic Union Party-- or maybe Free Republic could be in blue. We may have to try a few variations of that.
(3) I picked the red in the mock cover to connotate an emergency,
(4) I liked big bold fat font going across the full page so that it looks like a major warning sign, though note I was unable to extend each line flush all the way to the right which I think would have been better.
(5) I liked it better flush to left instead of centered.
(6) I picked the Harwick monument + a crowd for my mock cover, but a picture of a huge crowd protesting with a picture of the United States Congress in the background would be much better. DO NOT USE HARWICK. Obviously I would need it to be an open license or something I can pay a small amount to get. If you can find that picture then the page should probably be colored in red with Congress in white.
I got the idea 4 giant title from the book “seldom a quiet so bright” and Dellowby’s “When Freedom Fades” or “Grey Herons” by Mara Vostell though I hate that font)
I love Osric Thale’s “marked since the outset” cover so if you find a picture of Congress and a protest crowd instead of painting it red you could have just a couple of jagged red stripes going across it like that cover.
I love the 3-D effect of Greta Wolven's cover for The Silverwren where it looks like a page is being ripped. That effect could be done the words Free Republic like it's being torn off the page UPDATE: MANY DESIGNERS TRIED THAT & IT DID NOT WORK AT ALL.
Note that this book will be submitted to many award competitions, so please give me an award-winning cover.
I like how the title of the book The Unchosen by Martin Fellowes has the words starting to fade. I don't like the ladder on it, but maybe 'Free Republic' could fade like that.
Unionists

```html
<!DOCTYPE html>
<html lang="en">
<head>
<meta charset="utf-8">
<title>Final Hour to Rescue the Free Republic — Book Cover</title>
<link rel="stylesheet" href="https://fonts.googleapis.com/css2?family=Abril+Fatface&family=Josefin+Sans:wght@600&family=Poiret+One&display=swap">
<style>
  :root {
    --page: #ffffff;
    --frame: #7a7a7a;
    --sky-top: #c9cbcd;
    --sky-mid: #b7babd;
    --crowd-warm: #8c4a52;
    --crowd-cool: #50577a;
    --bar-red: rgba(236, 38, 52, 0.88);
    --bar-blue: rgba(68, 62, 168, 0.86);
    --title-ink: #ffffff;
    --navy: #27314f;
    --gold: #cfae3c;
    --name-band: #e8313b;
    --name-ink: #ffffff;
  }
  * { margin: 0; padding: 0; box-sizing: border-box; }
  html, body {
    width: 877px; height: 1200px; overflow: hidden;
    background: var(--page);
  }
  .canvas {
    position: relative; width: 877px; height: 1200px;
    background: var(--page);
    border: 1px solid #cfcfcf;
  }
  .cover {
    position: absolute; left: 39px; top: 34px;
    width: 800px; height: 1130px;
    background: var(--navy);
    outline: 1px solid var(--frame);
    overflow: hidden;
  }
  .cover-photo {
    position: absolute; left: 0; top: 0; width: 800px; height: 900px;
    background:
      linear-gradient(180deg, transparent 0%, transparent 42%, rgba(90,70,95,0.55) 60%, rgba(70,55,75,0.9) 100%),
      linear-gradient(90deg, var(--crowd-warm) 0%, var(--crowd-cool) 45%, #8a6c78 75%, #5c5f72 100%),
      var(--sky-mid);
    background-blend-mode: normal;
  }
  .cover-photo::before {
    content: ""; position: absolute; inset: 0 0 55% 0;
    background: linear-gradient(180deg, var(--sky-top), var(--sky-mid));
  }
  .title { position: absolute; left: 0; top: 0; }
  .title-bar {
    position: absolute; left: 0;
    display: flex; align-items: center;
    padding: 0 22px 0 64px;
    font-family: "Abril Fatface", serif;
    color: var(--title-ink);
    font-size: 112px; line-height: 1;
    letter-spacing: 1px;
    white-space: nowrap;
  }
  .title-bar--red { background: var(--bar-red); }
  .title-bar--blue { background: var(--bar-blue); }
  .title-bar--1 { top: 295px; height: 115px; }
  .title-bar--2 { top: 415px; height: 115px; }
  .title-bar--3 { top: 538px; height: 112px; }
  .title-bar--4 { top: 660px; height: 120px; }
  .title-bar--5 { top: 786px; height: 114px; }
  .subtitle {
    position: absolute; left: 0; top: 938px; width: 800px;
    text-align: center;
    font-family: "Josefin Sans", sans-serif; font-weight: 600;
    font-size: 23px; line-height: 32px; letter-spacing: 0.5px;
    color: var(--gold); text-transform: uppercase;
  }
  .author-band {
    position: absolute; left: 0; top: 1026px; width: 800px; height: 68px;
    background: var(--name-band);
    display: flex; align-items: center; justify-content: center;
  }
  .author-name {
    font-family: "Poiret One", sans-serif;
    font-size: 42px; letter-spacing: 15px;
    color: var(--name-ink); text-transform: uppercase;
    padding-left: 15px;
  }
</style>
</head>
<body>
<div class="canvas">
  <div class="cover">
    <div class="cover-photo" role="img" aria-label="Photograph of the United States Capitol dome under a grey sky, with a large crowd in winter clothing waving American flags in the foreground"></div>

    <h1 class="title">
      <span class="title-bar title-bar--red title-bar--1">FINAL</span>
      <span class="title-bar title-bar--blue title-bar--2">HOUR</span>
      <span class="title-bar title-bar--red title-bar--3">TO RESCUE</span>
      <span class="title-bar title-bar--blue title-bar--4">FREE</span>
      <span class="title-bar title-bar--red title-bar--5">REPUBLIC</span>
    </h1>

    <p class="subtitle">The Single Path to Halt the 2022 Partisan<br>Takeover &amp; Renew Our Homeland</p>

    <div class="author-band">
      <span class="author-name">Calder Finch Ostrom</span>
    </div>
  </div>
</div>
</body>
</html>
```